Veltora Software Business Card Design

We are a new organization called Veltora. We are a software as a service provider. We deliver a project and program management solution via the internet, so everyone has the ability to work together and collaborate. Its an enterprise platform and we will focus on 50 plus employee company.

We have a website in place
www.veltora-demo.com

Use this as a start of producing the business card. The logo is there as well, but if you have a great and better solution...

Color scheme's could be inline with the website, but don't pin point on it. We can always change the website, logo, color scheme etc.

Target Market(s)

B2B, Projectmembers, projectmanagers, ICT, CTO, Marketing Managers

Industry/Entity Type

Software

Requirements
Must have
• Marten Kuyvelsma

Tel: +31 255 47 09 36
Mob: +31 6 927 15 062
marten@veltora-demo.com
Oostelingpad 84c
2184 KT Zuiderhaven

Www.veltora-demo.com
social media links

```html
<!DOCTYPE html>
<html lang="en">
<head>
<meta charset="utf-8">
<title>Veltora Business Card</title>
<link rel="stylesheet" href="https://fonts.googleapis.com/css2?family=Quicksand:wght@400;500;600;700&display=swap">
<style>
  :root {
    --stage: #e9e9e7;
    --card-white: #fbfbfb;
    --lime: #b5d334;
    --orange: #f0821e;
    --ink: #555759;
    --ink-soft: #6b6d70;
    --slate-light: #9a9b9d;
    --slate-dark: #5d5e60;
    --white: #ffffff;
  }
  * { box-sizing: border-box; margin: 0; padding: 0; }
  html, body { width: 1200px; height: 1200px; overflow: hidden; }
  body {
    background: var(--stage);
    font-family: "Quicksand", sans-serif;
    position: relative;
  }
  .card {
    position: absolute;
    left: 250px;
    width: 700px;
    height: 453px;
    box-shadow: 0 10px 30px rgba(0,0,0,0.18);
    overflow: hidden;
  }
  /* Front */
  .card-front { top: 117px; background: var(--card-white); }
  .brand-band {
    position: absolute; left: 0; top: 0; bottom: 0;
    width: 220px;
    background: var(--lime);
  }
  .identity {
    position: absolute; left: 300px; top: 62px;
  }
  .person-name {
    font-size: 30px; font-weight: 700; letter-spacing: 2px;
    color: var(--ink); text-transform: uppercase;
    display: flex; align-items: center; gap: 26px;
    white-space: nowrap;
  }
  .person-name .accent-bar {
    width: 6px; height: 26px; background: var(--orange); display: inline-block;
  }
  .company {
    margin-top: 22px; margin-left: 60px;
  }
  .company-name {
    font-size: 36px; font-weight: 500; color: var(--orange); line-height: 1;
  }
  .company-web {
    font-size: 16px; font-weight: 600; color: var(--ink-soft); margin-top: 4px;
  }
  .contact-list {
    position: absolute; left: 430px; top: 272px;
    list-style: none;
    font-size: 16px; color: var(--ink-soft); font-weight: 500;
    line-height: 24px;
  }
  .contact-list li { display: flex; align-items: center; gap: 8px; white-space: nowrap; }
  .contact-list svg { width: 14px; height: 14px; flex: none; }
  .contact-list .indent { padding-left: 22px; }
  .contact-list strong { font-weight: 700; color: var(--ink); }
  /* Back */
  .card-back {
    top: 630px;
    background: radial-gradient(ellipse at 50% 40%, var(--slate-light) 0%, var(--slate-dark) 85%);
  }
  .back-name {
    position: absolute; left: 0; right: 0; top: 130px;
    text-align: center;
    font-size: 88px; font-weight: 400; color: var(--white); letter-spacing: 1px;
  }
  .social {
    position: absolute; display: flex; align-items: center; gap: 12px;
    font-size: 17px; font-weight: 700; color: var(--orange);
  }
  .social .dot {
    width: 26px; height: 26px; border-radius: 50%; background: var(--white);
  }
  .social-page { left: 340px; top: 350px; }
  .social-feed { left: 540px; top: 385px; }
</style>
</head>
<body>
  <section class="card card-front" aria-label="Business card front">
    <div class="brand-band"></div>
    <div class="identity">
      <h1 class="person-name">Marten Kuyvelsma <span class="accent-bar"></span></h1>
      <div class="company">
        <div class="company-name">Veltora</div>
        <div class="company-web">www.veltora-demo.com</div>
      </div>
    </div>
    <ul class="contact-list">
      <li><svg viewBox="0 0 14 14"><rect x="3" y="1" width="8" height="12" rx="1.5" fill="none" stroke="var(--orange)" stroke-width="1.6"/></svg>+31 255 47 09 36</li>
      <li><svg viewBox="0 0 14 14"><path d="M3 1 L6 1 L7 4 L5 5.5 Q6.5 8.5 8.5 9 L10 7 L13 8 L13 11 Q13 13 11 13 Q1 12 1 3 Q1 1 3 1Z" fill="var(--orange)"/></svg>+31 6 927 15 062</li>
      <li><svg viewBox="0 0 14 14"><rect x="1" y="3" width="12" height="8" fill="var(--orange)"/><path d="M1 3 L7 8 L13 3" fill="none" stroke="var(--white)" stroke-width="1.2"/></svg>marten@veltora-demo.com</li>
      <li><svg viewBox="0 0 14 14"><path d="M7 1 A4.5 4.5 0 0 1 11.5 5.5 Q11.5 8 7 13 Q2.5 8 2.5 5.5 A4.5 4.5 0 0 1 7 1Z" fill="var(--orange)"/><circle cx="7" cy="5.5" r="1.6" fill="var(--white)"/></svg>Oostelingpad 84c</li>
      <li class="indent">2184 KT&nbsp;<strong>Zuiderhaven</strong></li>
    </ul>
  </section>

  <section class="card card-back" aria-label="Business card back">
    <div class="back-name">Veltora</div>
    <div class="social social-page"><span class="dot"></span>VeltoraCOM</div>
    <div class="social social-feed"><span class="dot"></span>Veltora</div>
  </section>
</body>
</html>
```